Voyage Wellness Point Business Cards

We need business cards for our new start-up online travel health clinic. Visit our website voyagewellpoint.ca for branding and more info.

Target Market(s)

Travellers

Industry/Entity Type

Business

Contact Information for Business Card

Mara Kowalczyk
mara@voyagewellpoint.ca
+1 555 283 0461
voyagewellpoint.ca

Font styles to use
Sans Serif

Colors
f68d4d

```html
<!DOCTYPE html>
<html lang="en">
<head>
<meta charset="utf-8">
<title>Voyage Wellness Point – Business Cards</title>
<link rel="stylesheet" href="https://fonts.googleapis.com/css2?family=Lato:wght@400&family=Roboto:wght@500&family=Open+Sans:ital,wght@0,400;1,400&display=swap">
<style>
  :root {
    --brand-orange: #f4955a;
    --accent-orange: #f68d4d;
    --plane-grey: #b1b1b3;
    --card-black: #1c1c1c;
    --tagline-grey: #c9c9c9;
    --white: #ffffff;
    --backdrop: #ecebe8;
  }
  * { margin: 0; padding: 0; box-sizing: border-box; }
  html, body {
    width: 1200px; height: 900px; overflow: hidden;
    background: var(--backdrop);
  }
  .canvas { position: relative; width: 1200px; height: 900px; }

  .card { position: absolute; overflow: hidden; }

  /* Front card */
  .card-front {
    left: 178px; top: 75px; width: 588px; height: 364px;
    background: var(--brand-orange);
    font-family: "Lato", Arial, sans-serif;
    color: var(--white);
  }
  .front-artwork {
    position: absolute; left: 0; top: 0; width: 305px; height: 100%;
    background: linear-gradient(135deg, var(--plane-grey) 0%, #c4c4c6 55%, var(--plane-grey) 100%);
  }
  .holder-name {
    position: absolute; right: 36px; top: 58px;
    font-family: "Roboto", Arial, sans-serif; font-weight: 500;
    font-size: 23px; letter-spacing: 0.5px;
  }
  .contact-list {
    position: absolute; right: 37px; top: 249px;
    list-style: none; text-align: right;
    font-size: 16px; line-height: 21.5px;
  }
  .contact-list li { display: flex; justify-content: flex-end; align-items: center; gap: 5px; }
  .contact-icon { width: 13px; height: 13px; fill: var(--white); }

  /* Back card */
  .card-back {
    left: 388px; top: 505px; width: 567px; height: 352px;
    background: var(--card-black);
    font-family: "Open Sans", Verdana, sans-serif;
  }
  .brand-name {
    position: absolute; left: 0; right: 0; top: 150px; text-align: center;
    font-size: 33px; font-weight: 400; color: var(--accent-orange);
    letter-spacing: -0.3px;
  }
  .brand-tagline {
    position: absolute; right: 108px; top: 196px;
    font-size: 15px; font-style: italic; color: var(--tagline-grey);
  }
  .brand-url {
    position: absolute; left: 0; right: 0; top: 293px; text-align: center;
    font-size: 15px; letter-spacing: 1.6px; color: var(--accent-orange);
  }
</style>
</head>
<body>
<main class="canvas">

  <section class="card card-front">
    <div class="front-artwork" role="img" aria-label="Large white airplane silhouette on a grey field"></div>
    <h1 class="holder-name">MARA KOWALCZYK</h1>
    <ul class="contact-list">
      <li>+1 555 283 0461
        <svg class="contact-icon" viewBox="0 0 16 16" aria-hidden="true"><path d="M3.5 1.5l2.5 0 1.2 3-1.6 1.2a8 8 0 0 0 4.7 4.7l1.2-1.6 3 1.2v2.5c0 .8-.7 1.5-1.5 1.5A12.5 12.5 0 0 1 2 3c0-.8.7-1.5 1.5-1.5z"/></svg>
      </li>
      <li>mara@voyagewellpoint.ca
        <svg class="contact-icon" viewBox="0 0 16 16" aria-hidden="true"><path d="M1 3h14v10H1z M2 4.2v.5l6 4 6-4v-.5l-6 4z" fill-rule="evenodd"/></svg>
      </li>
      <li>www.voyagewellpoint.ca
        <svg class="contact-icon" viewBox="0 0 16 16" aria-hidden="true"><circle cx="8" cy="8" r="7"/><path d="M1 8h14M8 1c2.5 2.5 2.5 11.5 0 14M8 1c-2.5 2.5-2.5 11.5 0 14" stroke="#f4955a" stroke-width="1.1" fill="none"/></svg>
      </li>
    </ul>
  </section>

  <section class="card card-back">
    <p class="brand-name">Voyage Wellness Point</p>
    <p class="brand-tagline">Online Travel Health Experts</p>
    <p class="brand-url">www.voyagewellpoint.ca</p>
  </section>

</main>
</body>
</html>
```